Product Label Design for Natural Cosmetics brand

For our company Solmirena, we are looking for a completely new label design for our natural cosmetics line made with Organic Aloe Vera.
The first product in line is Travessa, our Aloe Vera Gel. Based on the schema you create, further labels would have to be created.
Since the line includes different products (for Face, Body, Hands, Sun), there should be some color distinction between different product that can keep the products apart, having still a very similar schema.
The label should reflect the South Portuguese (Algarve) way, trust and quality. The label design should be minimalistic, well recognizable and readable, including though the following components
Logo
Product Name: Travessa (medium)
Product Function (in Portuguese mainly): GEL DE ALOÉ VERA BIO (Large and visible)
Key Infomation: For Skin and Hair
Contains 200x concentrated Aloe Vera and Organic Jojoba Oil
Following logos are to be placed on the packaging: Vegan, Organic Aloe Vera, Natural Product
Additional Info:
Barcode (EAN Number)
Ingredients (please see the current label)
Made in Portugal
Address: Check current label
QR Code for URL to open Instructions and get support
Functions and Instructions need to be in the following language:
Function: Bio Aloe Vera Gel
Instruction: External Use.
English, Spanish, French, Italian, German, Dutch, Swedish, Portuguese, Arabic
Please use google translate or put placeholders for the respective languages.
I am uploading the current label (content and design is different than what we are looking for), the package (the amber pump bottle remains the same and is available to see at https://solmirena.example/default/travessa-aloe-vera-gel-1.html ) and the logo.
We would like you to illustrate how the label would look on the bottle and how you plan to distinct between other products that we will be designing in the series.
Please let me know if you need anything else.

```html
<!DOCTYPE html>
<html lang="en">
<head>
<meta charset="utf-8">
<title>Solmirena — Travessa Aloe Vera Gel label series</title>
<link href="https://fonts.googleapis.com/css2?family=Cinzel:wght@400;600&family=Montserrat:wght@300;400;500;700&family=Allura&display=swap" rel="stylesheet">
<style>
  :root {
    --page: #ffffff;
    --sand: #dccbc4;
    --rose: #eeaaae;
    --mint: #a9cbc4;
    --lagoon: #6c9fae;
    --title: #6e5a52;
    --leaf: #5f7a4b;
    --leaf-dark: #4d5e36;
    --ocean: #2f5d73;
    --aloe-light: #b7d39a;
    --aloe-deep: #6f9a4e;
    --wave-rose: #e9b3b4;
    --wave-sea: #a8c6cb;
  }
  * { margin: 0; padding: 0; box-sizing: border-box; }
  html, body { width: 1200px; height: 899px; overflow: hidden; background: var(--page); }
  .series { position: relative; width: 1200px; height: 899px; }

  .label {
    position: absolute; top: 360px; width: 234px; height: 352px;
    background: var(--sand); overflow: hidden;
    font-family: "Montserrat", sans-serif;
  }
  .label--skin-hair { left: 145px; --band: var(--rose); --wave: var(--wave-rose); --function: var(--leaf-dark); }
  .label--body { left: 480px; --band: var(--mint); --wave: var(--wave-sea); --function: var(--ocean); }
  .label--face { left: 815px; --band: var(--lagoon); --wave: var(--wave-sea); --function: var(--ocean); }

  .brand-band {
    position: absolute; left: 0; top: 0; width: 100%; height: 96px;
    background: var(--band);
    display: flex; align-items: center; justify-content: center; gap: 6px;
  }
  .brand-dot { width: 10px; height: 10px; border-radius: 50%; background: var(--leaf-dark); }
  .brand-name {
    font-weight: 500; font-size: 11px; letter-spacing: 2.5px;
    text-transform: uppercase; color: var(--leaf-dark);
  }

  .product-name {
    position: absolute; left: 0; width: 100%; top: 103px; text-align: center;
    font-family: "Cinzel", serif; font-weight: 600; font-size: 19px; letter-spacing: 1px;
    color: var(--title); line-height: 1;
  }
  .product-type {
    position: absolute; left: 20px; top: 120px;
    font-family: "Allura", cursive; font-size: 30px; color: var(--leaf); line-height: 1;
  }
  .product-function {
    position: absolute; left: 0; width: 100%; top: 142px; text-align: center;
    font-weight: 400; font-size: 30px; letter-spacing: 2px; line-height: 29px;
    color: var(--title); text-transform: uppercase;
  }
  .key-info {
    position: absolute; left: 22px; top: 210px;
    font-weight: 500; font-size: 8.5px; letter-spacing: 1.5px; line-height: 11px;
    color: var(--function); text-transform: uppercase;
  }
  .aloe-art {
    position: absolute; left: 112px; top: 208px; width: 100px; height: 52px;
    background: linear-gradient(160deg, var(--aloe-light), var(--aloe-deep));
    border-radius: 26px 6px 26px 6px;
  }
  .claim {
    position: absolute; left: 14px; top: 272px; width: 76px;
    font-weight: 700; font-size: 6px; line-height: 7.5px; color: var(--leaf-dark);
  }
  .badges { position: absolute; left: 102px; top: 275px; display: flex; gap: 14px; }
  .badge { width: 18px; height: 18px; border-radius: 50%; background: var(--leaf); opacity: 0.75; }
  .wave-pattern {
    position: absolute; left: 0; top: 310px; width: 100%; height: 24px;
    background: var(--wave); opacity: 0.55;
  }
</style>
</head>
<body>
<main class="series">

  <section class="label label--skin-hair">
    <div class="brand-band"><span class="brand-dot"></span><span class="brand-name">Solmirena</span></div>
    <h1 class="product-name">TRAVESSA</h1>
    <p class="product-type">gel</p>
    <p class="product-function">Aloé<br>Vera</p>
    <p class="key-info">For skin<br>and hair</p>
    <div class="aloe-art" role="img" aria-label="Illustration of cut aloe vera leaves"></div>
    <p class="claim">Contains 200x concentrated Aloe Vera and Organic Jojoba Oil</p>
    <div class="badges"><span class="badge"></span><span class="badge"></span><span class="badge"></span></div>
    <div class="wave-pattern" role="img" aria-label="Decorative sea wave pattern"></div>
  </section>

  <section class="label label--body">
    <div class="brand-band"><span class="brand-dot"></span><span class="brand-name">Solmirena</span></div>
    <h1 class="product-name">TRAVESSA</h1>
    <p class="product-type">gel</p>
    <p class="product-function">Aloé<br>Vera</p>
    <p class="key-info">For<br>body</p>
    <div class="aloe-art" role="img" aria-label="Illustration of cut aloe vera leaves"></div>
    <p class="claim">Contains 200x concentrated Aloe Vera and Organic Jojoba Oil</p>
    <div class="badges"><span class="badge"></span><span class="badge"></span><span class="badge"></span></div>
    <div class="wave-pattern" role="img" aria-label="Decorative sea wave pattern"></div>
  </section>

  <section class="label label--face">
    <div class="brand-band"><span class="brand-dot"></span><span class="brand-name">Solmirena</span></div>
    <h1 class="product-name">TRAVESSA</h1>
    <p class="product-type">gel</p>
    <p class="product-function">Aloé<br>Vera</p>
    <div class="aloe-art" role="img" aria-label="Illustration of cut aloe vera leaves"></div>
    <p class="claim">Contains 200x concentrated Aloe Vera and Organic Jojoba Oil</p>
    <div class="badges"><span class="badge"></span><span class="badge"></span><span class="badge"></span></div>
    <div class="wave-pattern" role="img" aria-label="Decorative sea wave pattern"></div>
  </section>

</main>
</body>
</html>
```